Design für ein Flyer mit Gutschein-Abriss
Zielgruppe
Handgemachte/ handgefertigte Körperpflege- und Kosmetikprodukte, die in kleinen Chargen gefertigt werden (somit wechselnde Produkte, die in bestimmten Mengen verfügbar sind) u.a. Seifen, Rasierseifen, Badezusätze, Gesichtspflege usw.
Die Produkte werden ohne künstliche Zusätze und Konservierungsstoffe hergestellt und erhalten so wenig Allergene-Stoffe wie möglich, zum Teil vegan.
In geringem Umfang werden ebenfalls Zubehör für Körperpflege vermarktet (z.B. Lavastein für Hornhautentfernung etc.).
Die Produkte werden online und im stationären Handel vertrieben.
Ansprechen von möglichst allen Altersgruppen.
Zielgruppe: 'Otto-Normal-Verbraucher', FRAUEN, Eltern (Mutter-Kind), Männer, in geringem Umfang Haustierbesitzer (Hundeshampoos etc.)
Aufgabenstellung
Größe: DinA5
Wir führen folgende Produkte in unserer Manufaktur:
Natürliche handgefertigte Naturseifen (Milchseifen, Kräuterseifen, Aromaseifen, uvm.), Seifentorten, Seifen- und Badecupcakes, handgerollte Badetrüffel, Badesalz, Badeöle, Badeeis, Badefondant, Körper- und Gesichtspflegeprodukte, Badezubehör, Aromatherapie, Dekorationsartikel sowie Geschenkkörbe für Privat- und Firmenkunden.
Die Produkte enthalten natürliche Inhaltsstoffe, zum Teil hochwertige ätherische Öle und sind Paraben- und SLS-frei. Unsere Produkte werden nicht an Tieren getestet. Wir achten bei der Auswahl der Inhaltsstoffe und unseren Lieferanten auf fairen Handel und nachhaltige Produktion.
Des Weiteren führen wir handgemachte Sojawachskerzen, diese sind Paraffin frei und enthalten Sojawachs aus nachhaltiger Produktion.
Der Flyer soll am unteren Rand den Gutschein beinhalten, welches abgeschnitten werden kann (mit 20 % Rabatt gilt für Online und im Laden).
Auf den Flyer sollten auf jeden Fall noch folgende Daten:
Neueröffnung am 05.05.2017
www.quorvalhaus.de
Öffnungszeiten: Freitags von 11:00 bis 18:00 Uhr
Anbei unser Logo so wie ein Link mit Bildern einiger unserer Produkte.
https://www.filetrunk-beispiel.de/sh/x81kqpwe3rd7h2t/ZZZ4mNbVtRKo2LPw8cY37XUhe?dl=0
Wir freuen uns schon auf viele tolle Vorschläge.

```html
<!DOCTYPE html>
<html lang="de">
<head>
<meta charset="utf-8">
<title>Quorvalhaus Naturals – Flyer mit Gutschein</title>
<link href="https://fonts.googleapis.com/css2?family=Yanone+Kaffeesatz:wght@300;400&family=Open+Sans:wght@700&display=swap" rel="stylesheet">
<style>
  :root {
    --green: #9bbb1c;
    --text-grey: #6d6d6d;
    --paper: #ffffff;
    --backdrop: #eceef2;
  }
  * { margin: 0; padding: 0; box-sizing: border-box; }
  html, body { width: 777px; height: 1200px; overflow: hidden; }
  body {
    background: var(--backdrop);
    font-family: "Yanone Kaffeesatz", "Arial Narrow", sans-serif;
    font-weight: 300;
    color: var(--text-grey);
    position: relative;
  }
  .sheet-slot {
    position: absolute;
    left: 182px;
    width: 412px;
    height: 578px;
    box-shadow: 0 2px 8px rgba(0,0,0,0.22);
    overflow: hidden;
  }
  .sheet-slot.front { top: 14px; }
  .sheet-slot.back { top: 608px; }
  .sheet {
    position: absolute;
    left: 0; top: 0;
    width: 480px;
    height: 673px;
    background: var(--paper);
    transform: scale(0.8583);
    transform-origin: top left;
  }
  .photo { position: absolute; }

  /* front */
  .brand-name {
    position: absolute; left: 0; width: 480px; top: 52px;
    text-align: center;
    font-size: 54px; font-weight: 300;
    color: var(--green); letter-spacing: 1px; line-height: 1;
    white-space: nowrap;
  }
  .tagline {
    position: absolute; left: 0; width: 480px; top: 132px;
    text-align: center; font-size: 16px; font-weight: 400;
    color: var(--text-grey); text-transform: uppercase; letter-spacing: .5px;
    white-space: nowrap;
  }
  .contact {
    position: absolute; left: 0; width: 480px;
    text-align: center; font-size: 12.5px; font-weight: 300;
    color: var(--green); white-space: nowrap;
  }
  .opening-badge {
    position: absolute; left: 335px; top: 295px; width: 145px; height: 60px;
    background: var(--green); color: #fff;
    font-family: "Open Sans", Arial, sans-serif; font-weight: 700;
    padding: 8px 0 0 12px;
  }
  .opening-badge .label { font-size: 12.5px; line-height: 1.2; }
  .opening-badge .date { font-size: 18px; line-height: 1.3; }
  .copy {
    position: absolute; left: 0; width: 480px;
    text-align: center; text-transform: uppercase;
    font-size: 15.5px; line-height: 23px;
    color: var(--text-grey);
  }
  .divider { position: absolute; left: 212px; width: 56px; height: 12px; }

  /* coupon */
  .coupon {
    position: absolute; left: 0; top: 600px; width: 480px; height: 73px;
    background: var(--green); color: #fff;
  }
  .cut-line { position: absolute; left: 0; top: 4px; width: 452px; height: 2px; }
  .scissors { position: absolute; left: 450px; top: -3px; width: 22px; height: 16px; }
  .coupon-brand {
    position: absolute; left: 20px; top: 20px;
    font-size: 30px; font-weight: 300; line-height: 1;
    white-space: nowrap;
  }
  .code-label {
    position: absolute; left: 167px; top: 22px; width: 141px;
    font-family: "Open Sans", Arial, sans-serif; font-size: 5.5px;
    text-transform: uppercase; text-align: center; letter-spacing: .2px;
    white-space: nowrap;
  }
  .code-field {
    position: absolute; left: 167px; top: 31px; width: 141px; height: 26px;
    background: #fff;
  }
  .discount {
    position: absolute; left: 318px; top: 14px; width: 140px;
    text-align: center; font-size: 31px; font-weight: 300; line-height: 1;
    text-transform: uppercase; white-space: nowrap;
  }
  .discount-note {
    position: absolute; left: 318px; top: 49px; width: 140px;
    text-align: center; font-size: 13px; line-height: 1.1;
    text-transform: uppercase; white-space: nowrap;
  }
</style>
</head>
<body>

<div class="sheet-slot front">
  <section class="sheet">
    <div class="brand-name">Quorvalhaus Naturals</div>
    <div class="tagline">Be natural with Quorvalhaus Naturals</div>
    <div class="contact" style="top:174px;">info@quorvalhaus.de • www.quorvalhaus.de – Lindenweg 12 • 91000 Musterstadt</div>
    <div class="contact" style="top:193px;">Öffnungszeiten: Freitags von 11:00 bis 18:00 Uhr</div>

    <div class="photo" role="img" aria-label="Handgerollte Badetrüffel mit Blütenblättern auf Silberteller, dahinter eine Blüte"
         style="left:0;top:217px;width:480px;height:168px;background:linear-gradient(100deg,#cfcfd2 0%,#e9e2cc 45%,#f2d6c8 80%,#f4e7a8 100%);"></div>
    <div class="opening-badge">
      <div class="label">Neueröffnung am</div>
      <div class="date">05.05.2017</div>
    </div>

    <p class="copy" style="top:398px;">Natürliche handgefertigte Naturseifen,<br>Körper- und Gesichtspflegeprodukte und Dekorationsartikel.</p>
    <div class="divider" role="img" aria-label="Kleines Blattornament" style="top:452px;background:linear-gradient(90deg,transparent,#cfe08f 20%,#cfe08f 80%,transparent);border-radius:6px;"></div>
    <p class="copy" style="top:474px;">Natürliche Inhaltsstoffe – 100% Paraben- und SLS-frei.</p>

    <div class="photo" role="img" aria-label="Gelber Badecupcake mit Sahnehaube"
         style="left:0;top:508px;width:151px;height:165px;background:linear-gradient(180deg,#f1f1f3,#f3ecb4 70%,#ece9ee);"></div>
    <div class="photo" role="img" aria-label="Naturseifenblock mit Lavendelmuster"
         style="left:151px;top:508px;width:165px;height:165px;background:linear-gradient(160deg,#ecebf0,#ddd3e6 45%,#e6d3b4 75%,#e9e7ee);"></div>
    <div class="photo" role="img" aria-label="Pinke Seife mit grünem Blattmotiv"
         style="left:316px;top:508px;width:164px;height:165px;background:linear-gradient(150deg,#eceaf0,#f4a7c3 50%,#eab6c8 80%,#e9e7ee);"></div>
  </section>
</div>

<div class="sheet-slot back">
  <section class="sheet">
    <div class="photo" role="img" aria-label="Gerollte Gästehandtücher als Biskuitrollen mit Kirschen"
         style="left:0;top:0;width:316px;height:170px;background:linear-gradient(120deg,#ecebf0,#d9c9a8 35%,#8a5a4a 55%,#f1ece6 80%,#e8e6ec);"></div>
    <div class="photo" role="img" aria-label="Kleine Badetörtchen und Cupcakes"
         style="left:316px;top:0;width:164px;height:170px;background:linear-gradient(160deg,#e6e2ec,#f6d56b 35%,#efb2bf 60%,#e7e2ec);"></div>

    <p class="copy" style="top:185px;">Badezubehör, Aromatherapie sowie Geschenkkörbe<br>für Privat- und Firmenkunden.</p>
    <div class="divider" role="img" aria-label="Kleines Blattornament" style="top:242px;background:linear-gradient(90deg,transparent,#cfe08f 20%,#cfe08f 80%,transparent);border-radius:6px;"></div>

    <div class="photo" role="img" aria-label="Handgemachte Sojawachskerzen in Gläsern mit Sahnehauben und Beeren"
         style="left:0;top:275px;width:480px;height:243px;background:linear-gradient(100deg,#eceaee 0%,#f1e6a8 15%,#c9e07a 28%,#cfa9d8 45%,#e07893 62%,#f2cbd8 80%,#e8a0b5 92%,#eceaee 100%);"></div>

    <p class="copy" style="top:531px;">Handgemachte Sojawachskerzen –<br>fairer Handel und nachhaltige Produktion.</p>

    <div class="coupon">
      <svg class="cut-line" viewBox="0 0 452 2" preserveAspectRatio="none" aria-hidden="true">
        <line x1="0" y1="1" x2="452" y2="1" stroke="#fff" stroke-width="2" stroke-dasharray="3 3"/>
      </svg>
      <svg class="scissors" viewBox="0 0 22 16" aria-hidden="true">
        <circle cx="4" cy="4" r="3" fill="none" stroke="#fff" stroke-width="1.4"/>
        <circle cx="4" cy="12" r="3" fill="none" stroke="#fff" stroke-width="1.4"/>
        <line x1="6.5" y1="5.5" x2="21" y2="12" stroke="#fff" stroke-width="1.4"/>
        <line x1="6.5" y1="10.5" x2="21" y2="4" stroke="#fff" stroke-width="1.4"/>
      </svg>
      <div class="coupon-brand">Quorvalhaus</div>
      <div class="code-label">Ihr persönlicher Gutscheincode</div>
      <div class="code-field"></div>
      <div class="discount">20 % Rabatt</div>
      <div class="discount-note">Online &amp; im Laden</div>
    </div>
  </section>
</div>

</body>
</html>
```